****Business Card Design for Cormorant Ridge. Design based around attached logo/company name

I’m looking for business card design for my company Cormorant Ridge Holdings,LLC. Design should be professional, sharp and minimal. Outside of the attached logos, greyscale colors for remainder of cards. My thoughts are two-sided card with attached logo on one side and my info on the other but open to one-sided as well with right design.
Target Market(s)
Real estate professionals including banks, private investors, property owners, developers, commercial tenants like Brewloft, Grocana or Tandberry’s.
Industry/Entity Type
Commercial real estate development and investments.
Contact Information for Business Card
Name, title, email, phone #’s, web address and physical address
Font styles to use
Other font styles liked:
- Helvetica, Garamond, etc
Colors
Designer to choose only greyscale colors for use in the design.
Requirements
Must have
- Attached logo first or second options.
Nice to have
- Two sided card with logo on one side. Attached Logo/company name can be laid out any way that flows as long as it’s legible.name
Should not have
- No loud colors. ***Please do not include logo, I have removed the company design with a logo image.

```html
<!DOCTYPE html>
<html lang="en">
<head>
<meta charset="utf-8">
<title>Cormorant Ridge Holdings – Business Card</title>
<link rel="stylesheet" href="https://fonts.googleapis.com/css2?family=Cormorant+Garamond:wght@500&family=Oswald:wght@500&family=Arimo:wght@400&display=swap">
<style>
  :root {
    --backdrop: #141414;
    --card: #232323;
    --card-edge: #2d2d2d;
    --ink-light: #f2f2f2;
    --ink-grey: #8c8f98;
    --ink-soft: #b9bbc0;
    --rule: #e6e6e6;
  }
  * { box-sizing: border-box; margin: 0; padding: 0; }
  html, body {
    width: 1200px; height: 900px; overflow: hidden;
    background: radial-gradient(ellipse at 50% 45%, #1d1d1d 0%, var(--backdrop) 70%);
  }
  .stage {
    position: relative; width: 1200px; height: 900px;
    display: flex; flex-direction: column; align-items: center; justify-content: center; gap: 40px;
  }
  .card {
    position: relative; width: 680px; height: 380px;
    background: linear-gradient(135deg, var(--card) 0%, #1e1e1e 55%, #2a2a2a 100%);
    border: 1px solid var(--card-edge);
    box-shadow: 0 18px 40px rgba(0,0,0,.6);
  }
  .card-front { display: flex; align-items: center; justify-content: center; }
  .brand-name {
    font-family: "Cormorant Garamond", Garamond, serif;
    font-weight: 500; font-size: 40px; letter-spacing: 2px;
    color: var(--ink-light); text-transform: uppercase; text-align: center; line-height: 1.15;
  }
  .card-back { display: flex; align-items: center; }
  .identity {
    width: 300px; text-align: right; padding-right: 26px;
  }
  .person-name {
    font-family: "Oswald", "Arial Narrow", sans-serif; font-weight: 500;
    font-size: 30px; letter-spacing: 1px; color: var(--ink-grey); text-transform: uppercase;
  }
  .person-title {
    font-family: "Arimo", Helvetica, Arial, sans-serif; font-size: 17px;
    color: var(--ink-light); margin-top: 4px;
  }
  .divider { width: 1.5px; height: 140px; background: var(--rule); }
  .contact {
    padding-left: 26px; font-family: "Arimo", Helvetica, Arial, sans-serif;
    font-size: 17px; letter-spacing: .8px; color: var(--ink-light); line-height: 1.35;
  }
  .address { margin-bottom: 10px; padding-left: 20px; }
  .contact-line { display: flex; align-items: center; gap: 8px; }
  .contact-line svg { width: 12px; height: 12px; flex: none; stroke: var(--ink-soft); fill: none; stroke-width: 1.4; }
</style>
</head>
<body>
<main class="stage">
  <section class="card card-front">
    <p class="brand-name">Cormorant Ridge<br>Holdings, LLC</p>
  </section>

  <section class="card card-back">
    <div class="identity">
      <p class="person-name">Daniel Whitcombe</p>
      <p class="person-title">Director</p>
    </div>
    <div class="divider"></div>
    <div class="contact">
      <p class="address">1186 Larkspur<br>Bend Corvale, OR 97480</p>
      <p class="contact-line">
        <svg viewBox="0 0 12 12"><path d="M3 1 L5 3.5 L4 5 Q5.5 7.5 7 8 L8.5 7 L11 9 L10 11 Q4 11 1 3 Z"/></svg>
        (541) 555-0192
      </p>
      <p class="contact-line">
        <svg viewBox="0 0 12 12"><rect x="1" y="2.5" width="10" height="7"/><path d="M1 2.5 L6 6.5 L11 2.5"/></svg>
        info@cormorantridge.com
      </p>
      <p class="contact-line">
        <svg viewBox="0 0 12 12"><circle cx="6" cy="6" r="5"/><ellipse cx="6" cy="6" rx="2.2" ry="5"/><path d="M1 6 H11"/></svg>
        www.cormorantridge.com
      </p>
    </div>
  </section>
</main>
</body>
</html>
```